Ridgeway Brew Label design/Graphic design

The Company
Ridgeway brew is an exciting new brand of ‘fit beer’ targeted at fitness enthusiasts as well as beer lovers. Ridgeway brew is a craft beer with added protein which can be used as a post work out recovery/leisure beverage. The target audience is generally male, 18-30 years old.
We need label/graphic design of the product to appear on our website www.ridgewaybrew.co.uk

The Project
The project is to submit four designs, one for each flavour:
• Larger
• Honey Ale
• Banana Ale
• Zero Alcohol

The design of each flavour must be differentiated, yet have a consistent theme throughout all flavours. At this point Ridgeway brew has no official logo so feel free to incorporate this into the design, although this is not absolutely necessary.

The label/design should include the following basic information:
Brand name: Ridgeway Brew
Type: Larger/Honey Ale/Banana Ale/Zero
Tag: 7g High Quality Protein
Alcohol percentage: 4%/Vol (0%/Vol for the Zero alcohol version)
Volume: 300ml

Brand Guidelines (designs not necessarily limited to these)
Font: Aldrich
Main Colours: Blue # 005fbf Orange # ed7000
Basic beer bottle image attached.

The final design will be displayed on (but not limited to) the website www.ridgewaybrew.co.uk

The winning designer may be contacted for future projects and opportunities with Ridgeway Brew.

Project Deadline Extended
Reason: My apologies I have been sick the last few days and have been unable to provide feedback. Your work is much appreciated, I will extend the project to give us a little more time and provide feedback individually later today. Best Regards, Oliver

Target Market(s)

The target audience is generally male, 18-30 years old.

Industry/Entity Type

Fitness

Requirements
Must have
• The label/design should include the following basic information:
Brand name: Ridgeway Brew
Volume: 300ml

```html
<!DOCTYPE html>
<html lang="en">
<head>
<meta charset="utf-8">
<title>Ridgeway Brew – Honey Ale Label</title>
<link rel="stylesheet" href="https://fonts.googleapis.com/css2?family=Krona+One&family=Oswald:wght@500&display=swap">
<style>
  :root {
    --paper: #ffffff;
    --banner-blue: #283a92;
    --badge-red: #b81d24;
    --badge-edge: #2a1a14;
    --cream: #f3e7cc;
    --honey-orange: #f39a1f;
    --tag-orange: #f2a23a;
    --figure-tan: #d9b25e;
    --glass-dark: #3a1f0c;
    --glass-mid: #a5581a;
    --glass-light: #d58a2a;
  }
  html, body {
    margin: 0;
    padding: 0;
    width: 1200px;
    height: 1100px;
    overflow: hidden;
    background: var(--paper);
  }
  .canvas {
    position: relative;
    width: 1200px;
    height: 1100px;
  }
  .artboard {
    position: absolute;
    left: 0;
    top: 0;
    width: 1200px;
    height: 1100px;
  }
  .banner { fill: var(--banner-blue); }
  .badge {
    fill: var(--badge-red);
    stroke: var(--badge-edge);
    stroke-width: 7;
    stroke-linejoin: round;
  }
  .mascot { fill: var(--figure-tan); }
  .brand-name {
    font-family: "Krona One", sans-serif;
    fill: var(--cream);
    text-anchor: middle;
  }
  .tagline {
    font-family: "Oswald", sans-serif;
    font-weight: 500;
    fill: var(--tag-orange);
    text-anchor: middle;
    letter-spacing: 2.5px;
    font-size: 15px;
  }
  .flavour {
    font-family: "Krona One", sans-serif;
    font-size: 62px;
    fill: var(--honey-orange);
    stroke: #ffffff;
    stroke-width: 5;
    paint-order: stroke fill;
    stroke-linejoin: round;
    text-anchor: middle;
  }
  .bottle { fill: url(#glass); }
  .neck-badge { fill: var(--banner-blue); }
</style>
</head>
<body>
<main class="canvas">
  <svg class="artboard" viewBox="0 0 1200 1100" xmlns="http://www.w3.org/2000/svg">
    <defs>
      <linearGradient id="glass" x1="0" y1="0" x2="1" y2="0">
        <stop offset="0" stop-color="var(--glass-dark)"/>
        <stop offset="0.3" stop-color="var(--glass-mid)"/>
        <stop offset="0.5" stop-color="var(--glass-light)"/>
        <stop offset="0.7" stop-color="var(--glass-mid)"/>
        <stop offset="1" stop-color="var(--glass-dark)"/>
      </linearGradient>

      <g id="honey-ale-label">
        <polygon class="banner" points="598,207 972,207 972,962 785,912 598,962"/>
        <polygon class="badge" points="785,335 1033,425 1033,630 785,765 537,630 537,425"/>
        <rect class="mascot" x="668" y="230" width="192" height="213" rx="14"/>
        <text class="brand-name" x="785" y="504" font-size="64">RIDGEWAY</text>
        <text class="brand-name" x="785" y="608" font-size="100">BREW</text>
        <text class="tagline" x="785" y="654">7G HIGH QUALITY PROTEIN</text>
        <text class="tagline" x="785" y="674">4% ALCOHOL VOLUME 300ML</text>
        <text class="flavour" x="785" y="835">HONEY</text>
        <text class="flavour" x="785" y="890">ALE</text>
      </g>
    </defs>

    <g class="bottle-mockup">
      <path class="bottle" role="img" aria-label="Photograph of an amber glass beer bottle with cap and condensation"
            d="M284,142 L368,142 L368,165 L361,170 L362,330 C368,400 432,430 432,500 L432,935 Q432,958 410,958 L244,958 Q222,958 222,935 L222,500 C222,430 286,400 291,330 L292,170 L284,165 Z"/>
      <polygon class="neck-badge" points="323,218 360,236 360,278 323,296 286,278 286,236"/>
      <rect class="mascot" x="307" y="232" width="32" height="52" rx="4"
            role="img" aria-label="Small strongman illustration"/>
      <use href="#honey-ale-label" transform="translate(54 471) scale(0.348)"/>
    </g>

    <g class="label-flat" role="group" aria-label="Honey Ale label">
      <use href="#honey-ale-label"/>
      <rect x="668" y="230" width="192" height="213" rx="14" fill="none"
            role="img" aria-label="Illustration of a mustachioed strongman lifting a barbell overhead"/>
    </g>
  </svg>
</main>
</body>
</html>
```